Flyer design

We need a marketing flyer to use when meeting with clients. We may also use it for mailings. Please see the attached document and images. Not all images need to be used. Please feel free to edit / photoshop images. Please also see our website : www.kelvorantissue.com

Industry/Entity Type

Marketing

```html
<!DOCTYPE html>
<html lang="en">
<head>
<meta charset="utf-8">
<title>Kelvoran Tissue Diagnostics — Flyer</title>
<link rel="stylesheet" href="https://fonts.googleapis.com/css2?family=Open+Sans:ital,wght@0,400;0,600;0,700;1,400&display=swap">
<style>
  :root{
    --orange:#f07f1e;
    --black:#0b0b0b;
    --ink:#2b2b2b;
    --white:#ffffff;
    --pink-deep:#b8456e;
    --pink-mid:#d98aa6;
    --pink-light:#efc6d2;
    --grey-light:#e4e4e4;
    --grey-mid:#b9b9b9;
    --plum:#3a2230;
    --red:#d8262f;
  }
  html,body{margin:0;padding:0;overflow:hidden;background:#fff;}
  .flyer{
    position:relative;width:927px;height:1200px;overflow:hidden;
    background:var(--black);font-family:"Open Sans",Arial,sans-serif;color:var(--ink);
  }
  .top-strip{position:absolute;left:0;top:0;width:927px;height:18px;background:var(--orange);}
  .hero-tissue{
    position:absolute;left:0;top:18px;width:927px;height:437px;
    background:linear-gradient(160deg,var(--pink-light) 0%,var(--pink-mid) 40%,var(--pink-deep) 75%,#8e3657 100%);
  }
  .hero-divider{
    position:absolute;left:0;top:448px;width:927px;height:14px;
    background:linear-gradient(90deg,var(--plum),#5b3648 60%,var(--plum));
  }
  .lab-scene{
    position:absolute;left:0;top:462px;width:927px;height:636px;
    background:linear-gradient(200deg,#8a8a8a 0%,var(--grey-mid) 30%,var(--grey-light) 55%,#f1f1f1 100%);
  }
  .curve-layer{position:absolute;left:0;top:0;}
  .intro{
    position:absolute;left:265px;top:0;width:425px;height:245px;box-sizing:border-box;
    padding:26px 14px 10px 14px;background:rgba(196,92,128,.55);
    color:var(--white);font-size:12.4px;line-height:17.6px;
  }
  .brand{
    position:absolute;left:0;top:68px;width:250px;height:235px;
    background:rgba(255,255,255,.82);
    display:flex;align-items:center;justify-content:center;gap:10px;
  }
  .brand-dot{width:18px;height:18px;border-radius:50%;background:var(--red);flex:none;}
  .brand-name{font-size:17px;font-weight:700;color:var(--ink);line-height:22px;width:170px;}
  .headline{
    position:absolute;left:45px;top:300px;margin:0;color:var(--white);
    font-size:36px;font-weight:700;line-height:48px;letter-spacing:.5px;
  }
  .headline .second{font-weight:600;display:block;}
  .services{position:absolute;left:90px;top:496px;width:420px;}
  .services .lead{margin:0 0 28px;font-size:19.5px;font-weight:600;line-height:25px;color:var(--ink);}
  .services .consult{margin:0;font-size:15px;font-weight:600;}
  .services .note{margin:2px 0 18px;font-size:11.5px;color:#555;}
  .services ul{margin:0;padding-left:22px;list-style:circle;font-size:14px;line-height:20px;}
  .since{position:absolute;left:90px;top:800px;margin:0;font-size:15px;font-style:italic;font-weight:600;}
  .stains{position:absolute;left:90px;top:846px;width:420px;margin:0;font-size:14px;line-height:20px;}
  .turnaround{position:absolute;left:90px;top:956px;width:260px;margin:0;font-size:14px;line-height:20px;}
  .portrait{
    position:absolute;left:690px;top:864px;width:190px;height:204px;box-sizing:border-box;
    border:6px solid var(--orange);
    background:linear-gradient(180deg,#e9e4dc 0%,#cfc7bb 55%,#2a2d3a 100%);
  }
  .credentials{
    position:absolute;right:250px;top:992px;margin:0;text-align:right;
    color:var(--orange);font-size:14.5px;line-height:19px;
  }
  .footer{position:absolute;left:0;top:1098px;width:927px;height:102px;background:var(--orange);color:var(--white);}
  .phone{position:absolute;left:0;width:927px;top:10px;display:flex;justify-content:center;align-items:center;gap:10px;font-size:22px;font-weight:600;}
  .address,.web{position:absolute;top:58px;display:flex;align-items:center;gap:10px;font-size:17px;}
  .address{left:42px;}
  .web{left:565px;}
  .icon{width:28px;height:28px;flex:none;}
</style>
</head>
<body>
<div class="flyer">
  <div class="top-strip"></div>
  <div class="hero-tissue" role="img" aria-label="Magnified pink-stained skin tissue section"></div>
  <div class="hero-divider"></div>
  <div class="lab-scene" role="img" aria-label="Soft-focus laboratory microscope scene"></div>

  <svg class="curve-layer" width="927" height="1200" viewBox="0 0 927 1200" aria-hidden="true">
    <path d="M927 18 L927 1098 L455 1098 C470 1000 480 950 500 900 C530 820 560 760 620 660 C660 590 690 540 725 480 C770 400 830 300 927 30 Z" fill="#0b0b0b"/>
    <path d="M455 1098 C470 1000 480 950 500 900 C530 820 560 760 620 660 C660 590 690 540 725 480 C770 400 830 300 927 30" fill="none" stroke="#f07f1e" stroke-width="10"/>
    <circle cx="745" cy="451" r="98" fill="#c9a98a" stroke="#f07f1e" stroke-width="8" role="img" aria-label="Microscope view of a thin tissue strip"/>
    <circle cx="545" cy="720" r="118" fill="#b0563f" stroke="#f07f1e" stroke-width="8" role="img" aria-label="Microscope view of stained tissue with rounded cells"/>
  </svg>

  <div class="brand">
    <span class="brand-dot"></span>
    <span class="brand-name">Kelvoran Tissue Diagnostics</span>
  </div>

  <p class="intro">We know how important reliable dermatopathology services are to your patients and your practice. As your partner in patient care, we want to do our part in helping you arrive at the diagnosis for each patient you entrust to us. We also know that part of our job is making working with us as smooth as possible. We can provide courier pick up service to local practices and we will help arrange overnight delivery for specimens sent from outside our area. We'll handle the details so you can focus on the care of your patients.</p>

  <h1 class="headline">THE DIAGNOSIS<span class="second">IN FOCUS</span></h1>

  <div class="services">
    <p class="lead">Commitment to helping find solutions, either in-house or through our contacts, for all your dermatopathology needs including but not limited to:</p>
    <p class="consult">Dermatopathology consultative service</p>
    <p class="note">[First or second opinions, off-site or on-site]</p>
    <ul>
      <li>Tissue processing</li>
      <li>Mohs technicians</li>
      <li>Immunohistochemistry and special stains</li>
    </ul>
  </div>

  <p class="since">Practicing Dermatopathology since 2007.</p>
  <p class="stains">Access to an extensive range of special and immunohistochemistry stains, and patient-centered consideration of the judicious use of them.</p>
  <p class="turnaround">Usually 2-3 day turnaround time depending on the circumstance of the case.</p>

  <p class="credentials">Lena M. Varga, MD.<br>Board Certified - Dermatopathology<br>Board Certified - Dermatology</p>
  <div class="portrait" role="img" aria-label="Portrait of the physician in a dark suit"></div>

  <div class="footer">
    <div class="phone">
      <svg class="icon" viewBox="0 0 28 28" aria-hidden="true"><circle cx="14" cy="14" r="14" fill="#3a2230"/><path d="M9.5 7.5l3 3-1.6 1.8c.9 1.9 2.3 3.3 4.2 4.2l1.8-1.6 3 3-1.9 2c-5.3-.6-9.8-5.1-10.4-10.4z" fill="#fff"/></svg>
      <span>800.555.0172</span>
    </div>
    <div class="address">
      <svg class="icon" viewBox="0 0 28 28" aria-hidden="true"><path d="M4 24V10h8V4h12v20z" fill="#3a2230"/><g fill="#f07f1e"><rect x="15" y="7" width="3" height="3"/><rect x="20" y="7" width="2" height="3"/><rect x="15" y="13" width="3" height="3"/><rect x="20" y="13" width="2" height="3"/><rect x="7" y="13" width="3" height="3"/><rect x="7" y="18" width="3" height="3"/></g></svg>
      <span>4120 W. Harbor Ave. # 212, Seal Point, CA 90000</span>
    </div>
    <div class="web">
      <svg class="icon" viewBox="0 0 28 28" aria-hidden="true"><circle cx="14" cy="14" r="13" fill="#3a2230"/><g fill="none" stroke="#fff" stroke-width="1.4"><circle cx="14" cy="14" r="9"/><ellipse cx="14" cy="14" rx="4" ry="9"/><path d="M5 14h18"/></g></svg>
      <span>www.kelvorantissue.com</span>
    </div>
  </div>
</div>
</body>
</html>
```